Anzeigengestaltung für Immobilienmakler
Zielgruppe
Immobilienmakler, Zielgruppe: Private (selten gewerbliche) Immobilienverkäufer/-käufer, Immobilienvermietung
Aufgabenstellung
Unser Logo soll Berücksichtigung finden, gerne auch wir als Personen. Design angelehnt an Logo und Schriftbild (siehe Anhang) und Website.
Headline: Ihre Immobilienvermittler für die Bodenseeregion.
Vorteile darstellen:
- Lokale Marktkenntnis: Wir kennen die Besonderheiten des regionalen Immobilienmarkts
-Persönliche Betreuung: Bei uns stehen Sie im Mittelpunkt
- Starkes Netzwerk: Profitieren Sie von unseren guten Beziehungen
- Kompletter Service: Von der ersten Beratung über die Erstellung des Exposés bis hin zur Vertragsabwicklung – wir bieten Ihnen alles aus einer Hand.
- Ausgebildet: GWA zertifizierte Immobilienmakler und Verbandszugehörigkeit
Kontaktdaten angeben:Festnetz/ Mobilfunknummer und Homepage, Ort: Salem
Das ganze in einem klaren und wertigen Design.
Die Anzeige soll sich im Text anpassen lassen und bitte in verschiedenen Formaten ausgeworfen werden (verschiedene Größen, ggf. kleinere Größen mit weniger textlichem Inhalt)

```html
<!DOCTYPE html>
<html lang="de">
<head>
<meta charset="utf-8">
<title>Ufer und Heim Immobilien – Anzeige</title>
<link href="https://fonts.googleapis.com/css2?family=Outfit:wght@400;500;600;700;800&display=swap" rel="stylesheet">
<style>
  :root {
    --navy: #2e466d;
    --navy-text: #2d4269;
    --slate: #7185a2;
    --slate-light: #8a9bb5;
    --paper: #ffffff;
    --mist: #eef2f7;
    --shadow-blue: #d7e0ee;
  }
  * { margin: 0; padding: 0; box-sizing: border-box; }
  html, body { width: 938px; height: 1200px; overflow: hidden; background: #fff; }
  body { font-family: "Outfit", sans-serif; color: var(--navy-text); }

  .ad { position: relative; width: 938px; height: 1200px; overflow: hidden; background: var(--paper); }
  .ad > * { position: absolute; }

  .backdrop { left: 0; top: 0; width: 938px; height: 1200px; }

  .interior-photo {
    left: 0; top: 13px; width: 938px; height: 700px;
    background: linear-gradient(160deg, #f1f3f6 0%, #f7f6f3 35%, #fbfbfb 65%, #ffffff 100%);
  }
  .team-photo {
    left: 10px; top: 400px; width: 520px; height: 560px;
    background: linear-gradient(180deg, rgba(220,226,236,0) 0%, #d9e0ea 45%, #c3cddd 100%);
    border-radius: 200px 200px 0 0;
  }

  .brand { left: 0; top: 170px; width: 938px; text-align: center; color: var(--navy-text); font-weight: 400; }
  .brand-mark { display: block; width: 70px; height: 70px; margin: -95px auto 20px; background: var(--slate); }
  .brand-name { font-size: 30px; letter-spacing: 0.5px; line-height: 1; }
  .brand-sub { font-size: 16px; letter-spacing: 6px; margin-top: 6px; line-height: 1; }

  .headline-box {
    left: 77px; top: 252px; width: 784px; height: 136px;
    background: var(--paper);
    box-shadow: 6px 6px 0 var(--shadow-blue);
    display: flex; align-items: center; justify-content: center;
  }
  .headline { font-weight: 800; font-size: 43px; line-height: 1.1; text-align: center; color: var(--navy-text); letter-spacing: 0.2px; }

  .benefits-title { left: 549px; top: 426px; font-size: 19px; font-weight: 700; color: var(--slate); }

  .benefit { left: 551px; width: 380px; display: flex; align-items: flex-start; }
  .benefit-icon { width: 60px; height: 60px; flex: none; margin-top: 2px; }
  .benefit-text { margin-left: 17px; }
  .benefit-title { font-size: 15.5px; font-weight: 700; color: var(--navy-text); line-height: 1.2; margin-bottom: 5px; }
  .benefit-body { font-size: 14px; font-weight: 400; color: var(--navy-text); line-height: 1.2; }

  .contact-title { left: 77px; top: 963px; font-size: 35px; font-weight: 700; color: #fff; }
  .contact-phone { left: 78px; top: 1026px; display: flex; align-items: center; color: #fff; }
  .contact-phone span { font-size: 44px; font-weight: 700; margin-left: 20px; letter-spacing: 0.3px; }
  .contact-line { display: flex; align-items: center; color: #fff; font-size: 19px; font-weight: 700; }
  .contact-line svg { margin-right: 28px; flex: none; }
  .contact-address { left: 78px; top: 1092px; }
  .contact-web { left: 78px; top: 1130px; }
  .contact-mail { left: 400px; top: 1130px; }

  .footer-brand { left: 770px; top: 1082px; width: 92px; text-align: center; color: #fff; font-size: 14px; font-weight: 600; line-height: 1.2; }
  .footer-brand i { display: block; width: 26px; height: 26px; margin: 0 auto 6px; background: #fff; }
</style>
</head>
<body>
<main class="ad">

  <div class="interior-photo" role="img" aria-label="Foto eines hellen Treppenhauses mit Hängeleuchten und Bildern an der Wand"></div>

  <svg class="backdrop" viewBox="215 265 1278 1653" preserveAspectRatio="none" aria-hidden="true">
    <rect x="215" y="265" width="518" height="18" fill="var(--slate)"/>
    <rect x="755" y="265" width="738" height="18" fill="var(--navy)"/>
  </svg>

  <div class="team-photo" role="img" aria-label="Porträtfoto der beiden Makler im Businessoutfit vor dem Treppenhaus"></div>

  <svg class="backdrop" viewBox="215 265 1278 1653" preserveAspectRatio="none" aria-hidden="true">
    <path d="M215,1530 C420,1440 640,1455 900,1545 C1150,1625 1360,1600 1493,1445 L1493,1918 L215,1918 Z" fill="var(--slate)"/>
    <path d="M215,1590 C420,1500 650,1520 900,1592 C1150,1660 1380,1660 1493,1555 L1493,1918 L215,1918 Z" fill="#ffffff"/>
    <path d="M215,1596 C420,1510 650,1530 900,1605 C1150,1678 1380,1680 1493,1572 L1493,1918 L215,1918 Z" fill="var(--navy)"/>
  </svg>

  <div class="brand">
    <i class="brand-mark"></i>
    <div class="brand-name">UFER UND HEIM</div>
    <div class="brand-sub">IMMOBILIEN</div>
  </div>

  <div class="headline-box">
    <h1 class="headline">IHRE IMMOBILIENVERMITTLER<br>FÜR DIE BODENSEE REGION</h1>
  </div>

  <h2 class="benefits-title">VORTEILE DARSTELLEN</h2>

  <div class="benefit" style="top:500px">
    <svg class="benefit-icon" viewBox="0 0 60 60"><circle cx="30" cy="30" r="30" fill="var(--slate)"/><path d="M30 15a9 9 0 0 1 9 9c0 7-9 15-9 15s-9-8-9-15a9 9 0 0 1 9-9z" fill="none" stroke="#fff" stroke-width="2"/><circle cx="30" cy="24" r="3.5" fill="none" stroke="#fff" stroke-width="2"/><ellipse cx="30" cy="41" rx="11" ry="3.5" fill="none" stroke="#fff" stroke-width="2"/></svg>
    <div class="benefit-text">
      <div class="benefit-title">LOKALE MARKTKENNTNIS</div>
      <div class="benefit-body">Wir kennen die<br>Besonderheiten des<br>regionalen Immobilienmarkts</div>
    </div>
  </div>

  <div class="benefit" style="top:579px">
    <svg class="benefit-icon" viewBox="0 0 60 60"><circle cx="30" cy="30" r="30" fill="var(--slate)"/><path d="M18 33v-5a12 12 0 0 1 24 0v5" fill="none" stroke="#fff" stroke-width="2"/><rect x="16" y="30" width="6" height="10" rx="3" fill="none" stroke="#fff" stroke-width="2"/><rect x="38" y="30" width="6" height="10" rx="3" fill="none" stroke="#fff" stroke-width="2"/><path d="M41 40c0 5-5 7-9 7" fill="none" stroke="#fff" stroke-width="2"/><circle cx="30" cy="47" r="2" fill="#fff"/></svg>
    <div class="benefit-text">
      <div class="benefit-title">KOMPLETTER SERVICE</div>
      <div class="benefit-body">Von der ersten Beratung über<br>die Erstellung des Exposés<br>bis hin zur Vertragsabwicklung</div>
    </div>
  </div>

  <div class="benefit" style="top:660px">
    <svg class="benefit-icon" viewBox="0 0 60 60"><circle cx="30" cy="30" r="30" fill="var(--slate)"/><g stroke="#fff" stroke-width="1.6" fill="none"><path d="M30 30L18 20M30 30L42 20M30 30L18 40M30 30L42 40M18 20L42 20"/><circle cx="30" cy="30" r="5" fill="var(--slate)"/><circle cx="18" cy="20" r="4" fill="var(--slate)"/><circle cx="42" cy="20" r="4" fill="var(--slate)"/><circle cx="18" cy="40" r="4" fill="var(--slate)"/><circle cx="42" cy="40" r="4" fill="var(--slate)"/></g></svg>
    <div class="benefit-text">
      <div class="benefit-title">STARKES NETZWERK</div>
      <div class="benefit-body">Profitieren Sie von unseren<br>guten Beziehungen</div>
    </div>
  </div>

  <div class="benefit" style="top:743px">
    <svg class="benefit-icon" viewBox="0 0 60 60"><circle cx="30" cy="30" r="30" fill="var(--slate)"/><g stroke="#fff" stroke-width="2" fill="none"><rect x="28" y="15" width="17" height="13"/><path d="M31 19h11M31 23h8M36 28l-4 12M38 28l4 12"/><circle cx="21" cy="22" r="3.5"/><path d="M15 43V32a6 6 0 0 1 12 0l3-4"/></g></svg>
    <div class="benefit-text">
      <div class="benefit-title">AUSGEBILDET</div>
      <div class="benefit-body">GWA zertifizierte Immobilien-<br>makler und Verbands-<br>zugehörigkeit</div>
    </div>
  </div>

  <div class="benefit" style="top:843px">
    <svg class="benefit-icon" viewBox="0 0 60 60"><circle cx="30" cy="30" r="30" fill="var(--slate)"/><g stroke="#fff" stroke-width="2" fill="none"><circle cx="31" cy="17" r="4"/><path d="M24 30a7 7 0 0 1 14 0z"/><path d="M13 36h6l6 2h8a2 2 0 0 1 0 4h-7M19 44l6 3h8l12-8a2 2 0 0 0-3-3l-7 4"/></g></svg>
    <div class="benefit-text">
      <div class="benefit-title">PERSÖNLICHE BETREUUNG</div>
      <div class="benefit-body">Bei uns stehen Sie im<br>Mittelpunkt</div>
    </div>
  </div>

  <h2 class="contact-title">Ihr Kontakt zu uns</h2>

  <div class="contact-phone">
    <svg width="30" height="30" viewBox="0 0 24 24"><path d="M6.6 2.5l3 3.2-1.8 2.6c1.2 2.7 3.2 4.7 5.9 5.9l2.6-1.8 3.2 3-1.6 3.4c-8.6-.3-14.4-6.1-14.7-14.7z" fill="var(--slate-light)"/></svg>
    <span>+49 (0)7544 5512093</span>
  </div>

  <div class="contact-line contact-address">
    <svg width="16" height="18" viewBox="0 0 16 18"><path d="M8 1a6 6 0 0 1 6 6c0 4.5-6 10-6 10S2 11.5 2 7a6 6 0 0 1 6-6z" fill="var(--slate-light)"/><circle cx="8" cy="7" r="2.3" fill="var(--navy)"/></svg>
    Lindenweg 4, 88697 Seewalden
  </div>

  <div class="contact-line contact-web">
    <svg width="16" height="16" viewBox="0 0 16 16"><g fill="none" stroke="var(--slate-light)" stroke-width="1.4"><circle cx="8" cy="8" r="6.5"/><ellipse cx="8" cy="8" rx="3" ry="6.5"/><path d="M1.5 8h13M2.5 4.8h11M2.5 11.2h11"/></g></svg>
    www.uferundheim.de
  </div>

  <div class="contact-line contact-mail">
    <svg width="16" height="16" viewBox="0 0 16 16"><circle cx="8" cy="8" r="8" fill="var(--slate-light)"/><rect x="3.5" y="5" width="9" height="6" fill="none" stroke="var(--navy)" stroke-width="1"/><path d="M3.5 5l4.5 3.5L12.5 5" fill="none" stroke="var(--navy)" stroke-width="1"/></svg>
    kontakt@uferundheim.de
  </div>

  <div class="footer-brand"><i></i>Ufer und Heim<br>Immobilien</div>

</main>
</body>
</html>
```